Flyer to Advertise Eyelash Extension Training Courses for Beauty Industry Professionals and Future

Hello,

I own an Eyelash and Skincare studio in Aliso Viejo, CA. www.velvetgloworks.com.We are now about to be offering a education side to our company where we offer courses to other beauty industry professionals or cosmetology students/future professionals. It will be called VGW ACADEMY. Our academies will have certain dates that will be on our website. I would like to make a flyer/menu of our new courses. You don't have to use all the information below but I've made it available for you. Please Re-word if necessary. Also you don't have to use the photos i've attached there just to help you see what I'm doing. Also I love the Look of Dora Whitfield brands, Lorvane, TEK, VILO, so I want this flyer to look really appealing to beauty industry professionals and future professionals.So be as creative as possible.

We have these courses:

1) Eyelash Enhancement Classic Extension Course
-1 Day Course. $350 and comes with a Kit that should last the students through 30 clients.
2) Eyelash Enhancement Russian Volume Course
-2 Day Course. $450 and comes with a kit that should last the students through 30 clients.
3)Threading Hair Removal Course
-1/2 Day course. $100 and comes with a kit that should last students through 60 clients. Students will need 3 Models for Eyebrow Threading
4)Spray Tanning Course
-1/2 Day course. $100 and will have an "add-on" kit that will get them a Spray tan Machine with 3 basic colors to last the student through 300 clients.

BUNDLE DEALS:
-Lash Pro Bundle: Students will learn Eyelash Enhancement Both Classic and Volume Extensions. 4 Day Course. $650 and comes with 2 kits for each technique.
-Velvet Pro Bundle: All of our courses combined. $850

MOBILE Options:
Call 949-387-6120 to inquire or email kelseyportland@velvetgloworks.com

Target Market(s)

Cosmetology Schools, Beauty Industry Students, Beauty industry professionals looking to seek add on services to provide to their clients.

Industry/Entity Type

Cosmetology

Font styles to use
Serif
Sans Serif
Decorative

Colors
f59296
f04a50
ffffff
000000
5c5c5c
aaaaaa

Requirements
Must have
• logo, all the courses, and our phone number email and address.
Nice to have
• pricing, and maybe saying something like, Additional courses insure that you are providing as many services as possible to your clients and in return you gain customer loyalty. (Reword)
Should not have
• cheesy.

```html
<!DOCTYPE html>
<html lang="en">
<head>
<meta charset="utf-8">
<title>VGW Academy – Courses Flyer</title>
<link rel="stylesheet" href="https://fonts.googleapis.com/css2?family=Tinos:wght@700&family=Lato:ital,wght@0,300;0,400;1,400&family=Gelasio:wght@700&family=Montserrat:wght@700&display=swap">
<style>
  :root {
    --pink: #f59296;
    --pink-soft: #e88a90;
    --red: #f04a50;
    --white: #ffffff;
    --black: #000000;
    --grey: #5c5c5c;
    --grey-light: #aaaaaa;
    --wine: rgba(120, 30, 38, 0.82);
  }
  html, body {
    margin: 0;
    padding: 0;
    overflow: hidden;
    background: var(--black);
  }
  .flyer {
    position: relative;
    width: 927px;
    height: 1200px;
    overflow: hidden;
    font-family: "Lato", sans-serif;
    color: var(--white);
    background: var(--black);
  }
  .hero-photo {
    position: absolute;
    inset: 0;
    background:
      linear-gradient(180deg, rgba(0,0,0,0) 60%, rgba(10,8,8,0.85) 76%, #141212 100%),
      linear-gradient(90deg, #050505 0%, #1a1212 30%, #5e3e34 48%, #a9826f 68%, #caa896 85%, #d6b8a7 100%);
  }
  .masthead-band {
    position: absolute;
    left: 0;
    top: 0;
    width: 522px;
    height: 176px;
    background: var(--wine);
  }
  .academy-name {
    position: absolute;
    left: 70px;
    top: 62px;
    margin: 0;
    font-family: "Lato", sans-serif;
    font-weight: 300;
    font-size: 40px;
    letter-spacing: 2px;
    line-height: 1;
    color: var(--pink-soft);
    white-space: nowrap;
  }
  .brand-name {
    position: absolute;
    right: 30px;
    top: 52px;
    font-family: "Montserrat", sans-serif;
    font-weight: 700;
    font-size: 19px;
    letter-spacing: 1px;
    color: var(--black);
  }
  .bundles {
    position: absolute;
    left: 0;
    top: 271px;
    width: 391px;
    height: 382px;
    background: rgba(34, 32, 32, 0.88);
  }
  .bundles h2 {
    position: absolute;
    left: 82px;
    top: 30px;
    margin: 0;
    font-weight: 300;
    font-size: 30px;
    color: var(--pink);
    letter-spacing: 0.3px;
  }
  .bundle {
    position: absolute;
    left: 86px;
    width: 300px;
  }
  .bundle h3 {
    margin: 0 0 9px;
    font-weight: 400;
    font-size: 21px;
    color: var(--pink);
  }
  .bundle p {
    margin: 0;
    font-size: 15.5px;
    line-height: 19px;
    font-weight: 300;
  }
  .bundle--lash { top: 93px; }
  .bundle--velvet { top: 251px; }
  .bundle--velvet h3 { margin-bottom: 2px; }
  .courses-label {
    position: absolute;
    left: 40px;
    top: 817px;
    width: 268px;
    height: 72px;
    background: linear-gradient(90deg, rgba(40,10,12,0.2) 0%, rgba(150,30,36,0.7) 65%, #a92c32 100%);
  }
  .courses-label span {
    position: absolute;
    left: 20px;
    top: 20px;
    font-size: 23px;
    font-weight: 300;
  }
  .course {
    position: absolute;
    width: 185px;
  }
  .course .kicker {
    margin: 0;
    font-family: "Tinos", serif;
    font-weight: 700;
    font-size: 14px;
  }
  .course h4 {
    margin: 0 0 17px;
    font-family: "Gelasio", serif;
    font-weight: 700;
    font-size: 20px;
    line-height: 22px;
    color: var(--pink);
  }
  .course p {
    margin: 0;
    font-size: 16px;
    line-height: 19px;
    font-weight: 300;
  }
  .course--classic { left: 48px; top: 911px; }
  .course--volume { left: 265px; top: 911px; }
  .course--threading { left: 484px; top: 916px; width: 180px; }
  .course--tanning { left: 700px; top: 921px; width: 178px; }
  .course--threading h4, .course--tanning h4 { margin-bottom: 15px; }
  .footer-rule {
    position: absolute;
    left: 0;
    top: 1137px;
    width: 927px;
    height: 11px;
    background: var(--grey);
  }
  .contact {
    position: absolute;
    left: 0;
    top: 1158px;
    width: 927px;
    text-align: center;
    font-size: 19px;
    font-weight: 300;
    color: var(--pink-soft);
  }
</style>
</head>
<body>
<main class="flyer">
  <div class="hero-photo" role="img" aria-label="Close-up beauty photograph of a woman's face with long eyelash extensions and a makeup brush"></div>

  <header class="masthead-band">
    <h1 class="academy-name">VGW ACADEMY</h1>
  </header>

  <div class="brand-name">VELVET GLOWORKS</div>

  <section class="bundles">
    <h2>BUNDLE DEALS</h2>
    <div class="bundle bundle--lash">
      <h3>Lash Pro Bundle:</h3>
      <p>Students will learn Eyelash Enhancement<br>Both Classic and Volume Extensions.<br>4 Day Course. $650<br>including 2 kits for each technique</p>
    </div>
    <div class="bundle bundle--velvet">
      <h3>Velvet Pro Bundle:</h3>
      <p><em>All</em> of our courses combined. $850</p>
    </div>
  </section>

  <div class="courses-label"><span>Courses Available</span></div>

  <article class="course course--classic">
    <p class="kicker">Eyelash Enhancement</p>
    <h4>Classic Extension Course</h4>
    <p>-1 Day Course. $350<br>includes a Kit that should<br>last the students<br>through 30 clients.</p>
  </article>
  <article class="course course--volume">
    <p class="kicker">Eyelash Enhancement</p>
    <h4>Russian Volume Course</h4>
    <p>-2 Day Course.$450<br>includes a kit that should<br>last the students<br>through 30 clients</p>
  </article>
  <article class="course course--threading">
    <h4>Threading Hair Removal Course</h4>
    <p>-1/2 Day course $100<br>includes a kit that should<br>last the students<br>through 60 clients.<br>Students will need 3<br>Models for Eyebrow<br>Threading</p>
  </article>
  <article class="course course--tanning">
    <h4>Spray Tanning Course</h4>
    <p>-1/2 Day course $100<br>includes an "add-on" kit<br>that will get the student<br>a Spray tan Machine<br>with 3 basic colors to<br>last the through<br>300 clients</p>
  </article>

  <div class="footer-rule"></div>
  <footer class="contact">Call 949-387-6120 to inquire or email kelseyportland@velvetgloworks.com</footer>
</main>
</body>
</html>
```